Tidal Care Works Site Re-Design

Review content of current website www.tidalcareworks-example.com and re-design each page - I have attached a comprehensive website brief which outlines the products and services that tidal care works sells online, the type of style I like my website to be in which is clean, uncluttered, professional and modern, it also indicates which other websites that I admire and that I would like my existing site to be changed to that style. The Personal Trainer Development Sub Page is going to be re -written and I am hoping that the new design will make my site more modern and provide a better user experience. I would also be open if the designer wanted to use their creative talents to re-design my logo if you think you could do a better job. I look forward to seeing some awesome designs.

Target Market(s)

Refer to attached design brief

Industry/Entity Type

Health And Wellness

Number of Pages Required

5+ page

Colors
9bcb3c
6b449b

Requirements
Must have
• Refer to design brief
Nice to have
• Refer to design brief
Should not have
• Refer to design brief

```html
<!DOCTYPE html>
<html lang="en">
<head>
<meta charset="utf-8">
<title>Tidal Care Works – Home</title>
<link href="https://fonts.googleapis.com/css2?family=Montserrat:wght@400;600;700;800&family=Open+Sans:wght@400;600;700&display=swap" rel="stylesheet">
<style>
:root{
  --green:#9bcb3c;
  --purple:#6b449b;
  --ink:#111111;
  --text:#555555;
  --muted:#8a8a8a;
  --rule:#2a2a2a;
  --dark:#1f1f1f;
  --darker:#161616;
  --navy:#243049;
  --white:#ffffff;
}
*{box-sizing:border-box;margin:0;padding:0}
html,body{width:1200px;height:5325px;overflow:hidden;background:var(--white)}
body{position:relative;font-family:"Open Sans",Arial,sans-serif;color:var(--text);font-size:13px;line-height:1.7}
.abs{position:absolute}
h1,h2,h3,h4,.head{font-family:"Montserrat",Arial,sans-serif;color:var(--ink)}
.slash{color:var(--green)}
.eyebrow{font-family:"Montserrat",Arial,sans-serif;font-size:11px;font-weight:700;letter-spacing:.5px;text-transform:uppercase;color:var(--green)}
.section-title{font-size:38px;font-weight:800;text-transform:uppercase;letter-spacing:.5px;text-align:center;width:1200px;left:0}
.btn{display:inline-block;background:var(--green);color:var(--ink);font-family:"Montserrat",Arial,sans-serif;font-weight:700;font-size:11px;text-transform:uppercase;letter-spacing:.8px;border-radius:22px;text-align:center}
.photo{display:block}

/* hero */
.hero{top:0;left:0;width:1200px;height:728px;background:linear-gradient(180deg,#3a3538 0%,#5a4a44 45%,#2b2628 100%)}
.hero-glow{top:0;left:360px;width:520px;height:640px;background:radial-gradient(ellipse at 50% 40%,rgba(210,170,140,.45),rgba(0,0,0,0) 70%)}
.brand{top:30px;left:100px;font-family:"Montserrat",Arial,sans-serif;font-weight:700;font-size:24px;color:var(--green);letter-spacing:1px}
.nav{top:36px;right:45px;display:flex;gap:36px;font-family:"Montserrat",Arial,sans-serif;font-size:12px;font-weight:600;text-transform:uppercase;color:var(--white)}

/* feature cards */
.card{width:280px}
.card .photo{height:150px;background:linear-gradient(135deg,#5b5f64,#8d7f74)}
.card-label{height:88px;background:var(--dark);padding:22px 22px}
.card-label .eyebrow{font-size:11px}
.card-label h3{color:var(--white);font-size:19px;font-weight:600;text-transform:uppercase;letter-spacing:.5px;margin-top:4px}
.card p{margin-top:16px;padding:0 22px;font-size:13px;color:var(--text)}
.card .rule{margin-top:28px;height:3px;background:var(--rule)}

/* trainer */
.trainer-title{top:970px;left:128px;font-size:40px;font-weight:800;text-transform:uppercase}
.trainer-hi{top:1035px;left:128px;font-size:16px;color:var(--ink)}
.trainer-copy{top:1085px;left:128px;width:400px;font-size:13px}
.trainer-photo{top:923px;left:657px;width:375px;height:462px;background:linear-gradient(180deg,#3a3f46,#1d2230 60%,#262a33)}

/* video band */
.video-band{top:1420px;left:0;width:1200px;height:462px;background:linear-gradient(90deg,#2d2022 0%,#4a3436 45%,#2a2426 100%)}
.video-band h2{position:absolute;top:205px;left:611px;color:var(--white);font-size:40px;font-weight:800;text-transform:uppercase}

/* services */
.service{width:295px;text-align:center}
.service h4{font-size:15px;font-weight:700;text-transform:uppercase;line-height:1.5;height:48px}
.service p{margin-top:12px;padding:0 20px;font-size:13px}
.service .rule{position:absolute;top:203px;left:0;width:295px;height:3px;background:var(--rule)}

/* fuel */
.fuel{top:2439px;left:0;width:1200px;height:401px;background:var(--navy)}
.fuel h2{position:absolute;top:185px;left:128px;color:var(--white);font-size:38px;font-weight:800;text-transform:uppercase}
.fuel-photo{position:absolute;top:0;left:550px;width:650px;height:401px;background:radial-gradient(ellipse at 45% 55%,#f4f1ec 0%,#efb48a 38%,#c34e5a 55%,#2c3a56 78%)}

/* tips */
.tips-title{top:2965px;left:0;width:1200px;text-align:center;font-size:36px;font-weight:800;text-transform:uppercase}
.tips-eyebrow{top:3035px;left:0;width:1200px;text-align:center}
.tips-sub{top:3065px;left:0;width:1200px;text-align:center;font-size:17px;color:var(--ink)}
.tips-copy{top:3128px;left:170px;width:860px;text-align:center;font-size:13px}
.signup{top:3223px;left:121px;width:962px;height:238px;border:4px solid var(--ink)}
.field{position:absolute;top:56px;width:400px;border-bottom:1px solid #d8d8d8;padding-bottom:22px;font-family:"Montserrat",Arial,sans-serif;font-size:13px;font-weight:600;color:var(--ink)}
.signup .btn{position:absolute;top:160px;left:390px;width:168px;height:40px;line-height:40px}

/* testimonials */
.testimonials{top:3525px;left:0;width:1200px;height:476px;background:var(--dark)}
.testimonials h2{position:absolute;top:72px;left:0;width:1200px;text-align:center;color:var(--white);font-size:38px;font-weight:800;text-transform:uppercase}
.quote{position:absolute;top:168px;width:300px;text-align:center}
.avatar{width:96px;height:96px;border-radius:50%;margin:0 auto;background:radial-gradient(circle at 50% 45%,#c79b80,#6a4a3c)}
.quote h4{margin-top:20px;color:var(--white);font-size:13px;font-weight:700;text-transform:uppercase}
.quote p{margin-top:8px;color:#b8b8b8;font-size:12.5px}

/* blog */
.blog-title{top:4075px}
.post{width:290px}
.post .photo{height:168px;background:linear-gradient(135deg,#e9e6e2,#b7a79c 55%,#5a4b45)}
.post .eyebrow{margin-top:22px;display:block}
.post h3{margin-top:6px;font-size:17px;font-weight:800;text-transform:uppercase;line-height:1.3}
.post p{margin-top:16px;font-size:13px}
.post .more{margin-top:22px;font-family:"Montserrat",Arial,sans-serif;font-size:11px;font-weight:600;text-transform:uppercase;color:var(--ink)}
.post .rule{margin-top:22px;height:3px;background:var(--rule)}

/* footer */
.footer{top:4810px;left:0;width:1200px;height:515px;background:var(--darker);color:#bdbdbd}
.footer .col{position:absolute;top:68px}
.footer h5{font-family:"Montserrat",Arial,sans-serif;color:var(--white);font-size:15px;font-weight:700;text-transform:uppercase;letter-spacing:.5px}
.footer .brand-foot{font-family:"Montserrat",Arial,sans-serif;font-size:21px;font-weight:700;color:var(--green);line-height:1.2;white-space:nowrap}
.footer p{font-size:13px;color:#bdbdbd}
.hours{margin-top:26px;width:200px;font-size:12px}
.hours div{display:flex;justify-content:space-between;padding:10px 0;border-bottom:1px solid #2c2c2c}
.hours .today{color:var(--white);font-weight:700}
.contact-big{font-family:"Montserrat",Arial,sans-serif;color:var(--white);font-size:20px;font-weight:600;margin-top:78px}
.copyright{position:absolute;top:468px;left:128px;font-size:12px;color:#bdbdbd}
</style>
</head>
<body>

<!-- hero -->
<header class="abs hero" role="img" aria-label="Photo of a woman in a gym wearing a sports top, exercise bikes and weights behind her"></header>
<div class="abs hero-glow"></div>
<div class="abs brand">Tidal Care Works</div>
<nav class="abs nav"><span>Classes</span><span>Schedule</span><span>Elements</span><span>Features</span><span>Blog</span></nav>

<section>
  <article class="abs card" style="top:490px;left:128px">
    <div class="photo" role="img" aria-label="Photo of two women doing a yoga stretch"></div>
    <div class="card-label"><div class="eyebrow">Flexibility</div><h3>Yoga</h3></div>
    <p>Short yoga sessions that build balance, ease stiff joints and help you recover between harder training days.</p>
    <div class="rule"></div>
  </article>
  <article class="abs card" style="top:490px;left:460px">
    <div class="photo" role="img" aria-label="Photo of a woman lifting a dumbbell"></div>
    <div class="card-label"><div class="eyebrow">Workout</div><h3>Dumbbell</h3></div>
    <p>Simple dumbbell routines for strength at any level, coached step by step so every rep counts safely.</p>
    <div class="rule"></div>
  </article>
  <article class="abs card" style="top:490px;left:792px">
    <div class="photo" role="img" aria-label="Photo of a woman performing squats in a gym"></div>
    <div class="card-label"><div class="eyebrow">Legs</div><h3>Squats</h3></div>
    <p>Squat drills that power your legs and core, with form tips to keep knees and back well protected.</p>
    <div class="rule"></div>
  </article>
</section>

<!-- trainer -->
<section>
  <div class="abs eyebrow" style="top:935px;left:128px">Professional Trainer</div>
  <h2 class="abs trainer-title">Your Trainer <span class="slash">/</span></h2>
  <p class="abs trainer-hi">Hi there, my name is Marcus Hale.</p>
  <p class="abs trainer-copy">I would like to share what I have learnt over the past few years with you to help you become the best that you can be. During my fitness journey I have developed a passion for real food and have also brought this into my daily life.</p>
  <span class="abs btn" style="top:1240px;left:128px;width:212px;height:40px;line-height:40px">Read More</span>
  <div class="abs trainer-photo" role="img" aria-label="Portrait photo of the personal trainer in a navy T-shirt"></div>
</section>

<!-- training videos -->
<section class="abs video-band" role="img" aria-label="Photo of a person training on gym equipment, darkened">
  <h2>Training Videos <span class="slash">/</span></h2>
</section>

<!-- services -->
<section>
  <h2 class="abs section-title" style="top:1952px">Services <span class="slash">/</span></h2>
  <div class="abs service" style="top:2090px;left:128px">
    <h4>PT Development and Coaching</h4>
    <p>We provide business development training courses for those already operating within the health and fitness industry.</p>
    <div class="rule"></div>
  </div>
  <div class="abs service" style="top:2090px;left:453px">
    <h4>Customized Nutrition and Training</h4>
    <p>We have a wide range of training programs ranging from weight loss, strength and toning through to general fitness.</p>
    <div class="rule"></div>
  </div>
  <div class="abs service" style="top:2090px;left:778px">
    <h4>Fitness Courses &amp; Education</h4>
    <p>Tidal Care Works can provide you with not only the best education but will also provide a clear pathway to work experience in real gyms post course.</p>
    <div class="rule"></div>
  </div>
</section>

<!-- fuel your body -->
<section class="abs fuel">
  <h2>Fuel Your Body <span class="slash">/</span></h2>
  <div class="fuel-photo" role="img" aria-label="Photo of a white platter of sliced fresh fruit: dragon fruit, kiwi, orange, melon and blueberries"></div>
</section>

<!-- tips / download -->
<section>
  <h2 class="abs tips-title">10 Tips to Motivate Yourself to Succeed <span class="slash">/</span></h2>
  <div class="abs eyebrow tips-eyebrow">Free Download</div>
  <p class="abs tips-sub">Fully Customized Training &amp; Nutrition Programs for everyone</p>
  <p class="abs tips-copy">If your goal is to undertake a new training program, start a new diet or begin building your own business, it is simple to read our report as a MUST to help mentally prepare you!</p>
  <form class="abs signup">
    <div class="field" style="left:36px">Your Full Name</div>
    <div class="field" style="left:520px">Your E-Mail</div>
    <span class="btn">Download Now</span>
  </form>
</section>

<!-- testimonials -->
<section class="abs testimonials">
  <h2>Testimonials <span class="slash">/</span></h2>
  <div class="quote" style="left:128px">
    <div class="avatar" role="img" aria-label="Round portrait photo of a client"></div>
    <h4>Daniel Foster</h4>
    <p>The coaching gave me a clear plan and real results within weeks. I finally enjoy training and feel stronger every single day.</p>
  </div>
  <div class="quote" style="left:450px">
    <div class="avatar" role="img" aria-label="Round portrait photo of a client"></div>
    <h4>Lena Moreau</h4>
    <p>Friendly, expert support from day one. The nutrition guide changed how I eat and I have more energy than ever before.</p>
  </div>
  <div class="quote" style="left:772px">
    <div class="avatar" role="img" aria-label="Round portrait photo of a client"></div>
    <h4>Grace Whitley</h4>
    <p>The course prepared me fully for my new career. Great mentors, practical lessons and a clear path into real gym work.</p>
  </div>
</section>

<!-- blog -->
<section>
  <h2 class="abs section-title blog-title">Blog <span class="slash">/</span></h2>
  <article class="abs post" style="top:4189px;left:110px">
    <div class="photo" role="img" aria-label="Photo of people cycling on exercise bikes in a bright studio"></div>
    <span class="eyebrow">January 8, 2017</span>
    <h3>Healthy Nutrition to Boost Your Gains</h3>
    <p>Simple meal ideas packed with protein and fresh produce to fuel training and speed up your recovery.</p>
    <div class="more">Read More</div>
    <div class="rule"></div>
  </article>
  <article class="abs post" style="top:4189px;left:455px">
    <div class="photo" role="img" aria-label="Photo of people cycling on exercise bikes in a bright studio"></div>
    <span class="eyebrow">January 8, 2017</span>
    <h3>Healthy Nutrition to Boost Your Gains</h3>
    <p>Simple meal ideas packed with protein and fresh produce to fuel training and speed up your recovery.</p>
    <div class="more">Read More</div>
    <div class="rule"></div>
  </article>
  <article class="abs post" style="top:4189px;left:800px">
    <div class="photo" role="img" aria-label="Photo of people cycling on exercise bikes in a bright studio"></div>
    <span class="eyebrow">January 8, 2017</span>
    <h3>Healthy Nutrition to Boost Your Gains</h3>
    <p>Simple meal ideas packed with protein and fresh produce to fuel training and speed up your recovery.</p>
    <div class="more">Read More</div>
    <div class="rule"></div>
  </article>
</section>

<!-- footer -->
<footer class="abs footer">
  <div class="col" style="left:128px;width:210px">
    <div class="brand-foot">Tidal Care Works</div>
    <p style="margin-top:22px;width:170px">Practical coaching, nutrition and education for people who want to train smarter and live well. Join our community today.</p>
  </div>
  <div class="col" style="left:369px">
    <h5>Opening Hours /</h5>
    <div class="hours">
      <div><span>Monday</span><span>07:00-17:00</span></div>
      <div><span>Tuesday</span><span>07:00-17:00</span></div>
      <div><span>Wednesday</span><span>07:00-17:00</span></div>
      <div><span>Thursday</span><span>07:00-17:00</span></div>
      <div class="today"><span>Friday</span><span>07:00-17:00</span></div>
      <div><span>Saturday</span><span>07:00-17:00</span></div>
      <div><span>Sunday</span><span>07:00-17:00</span></div>
    </div>
  </div>
  <div class="col" style="left:614px">
    <h5>Latest Posts /</h5>
  </div>
  <div class="col" style="left:855px;width:260px">
    <h5>Contact /</h5>
    <div class="contact-big">0800 555 0142</div>
    <p>Mobile available 24 hours</p>
    <div class="contact-big" style="margin-top:70px">Email Us</div>
    <p>hello@tidalcareworks-example.com</p>
  </div>
  <div class="copyright">Copyright 2018 by Tidal Care Works</div>
</footer>

</body>
</html>
```